Harborline Energy - needs a business card

Harborline Energy is a U.S. based diesel sourcing and distribution company that supports American oil & gas fields through providing quality product and consistent services.

Target Market(s)

Oil and Gas

Contact Information for Business Card

The background of the card must be white to ensure the logo pops.

Font styles to use
Serif
Sans Serif

Colors

Designer to choose colors to be used in the design.

Requirements
Must have
• Front of Card: Tag line: Harborline Energy, Powering America's Oil & Gas fields.
• Not sure if you guys do this part but just in case...
• Dale Menschow
• Owner/CEO
• C:555.318.4076
• E:Dmenschow@harborlineenergy.example
• W:Harborlineenergy.example
• Locations: Servicing the Powder River, DJ basin and Bakken formations.
• Back of Card: " Frac fueling is what we do. We understand how important diesel fuel is to your operation, which is why our main service line is Frac fueling. We assure our supply and stand by our service"

```html
<!DOCTYPE html>
<html lang="en">
<head>
<meta charset="utf-8">
<title>Harborline Energy – Business Card</title>
<link href="https://fonts.googleapis.com/css2?family=Montserrat:wght@700;800&family=Open+Sans:wght@400;600;700&display=swap" rel="stylesheet">
<style>
  :root {
    --navy: #153a72;
    --navy-deep: #0b2752;
    --red: #c8161d;
    --ink: #3d3d3d;
    --rule: #8a8a8a;
    --paper: #ffffff;
    --stage: #e6e7ea;
  }
  * { box-sizing: border-box; margin: 0; padding: 0; }
  html, body { width: 1200px; height: 892px; overflow: hidden; }
  body {
    background: var(--stage);
    font-family: "Open Sans", Arial, sans-serif;
    display: flex;
    align-items: center;
    justify-content: center;
    gap: 40px;
  }
  .card {
    position: relative;
    width: 560px;
    height: 320px;
    overflow: hidden;
    box-shadow: 0 6px 18px rgba(0,0,0,.18);
  }

  /* Back of card */
  .card-back {
    background: radial-gradient(ellipse at 50% 25%, #24528f 0%, var(--navy) 45%, var(--navy-deep) 100%);
    color: #fff;
    text-align: center;
  }
  .back-brand {
    position: absolute;
    top: 88px; left: 0; right: 0;
    display: flex; align-items: center; justify-content: center; gap: 12px;
    font-family: "Montserrat", Arial, sans-serif;
    font-weight: 800;
    font-size: 28px;
    letter-spacing: .5px;
  }
  .brand-dot { width: 18px; height: 18px; border-radius: 50%; background: #fff; }
  .tagline {
    position: absolute;
    top: 176px; left: 0; right: 0;
    display: flex; align-items: center; justify-content: center; gap: 10px;
    font-weight: 700;
    font-size: 15px;
  }
  .tagline::before, .tagline::after {
    content: ""; width: 40px; height: 1px; background: #fff;
  }
  .back-copy {
    position: absolute;
    top: 204px; left: 50px; right: 50px;
    font-size: 10px;
    line-height: 1.5;
    opacity: .95;
  }

  /* Front of card */
  .card-front { background: var(--paper); }
  .front-brand {
    position: absolute;
    top: 54px; right: 36px;
    display: flex; align-items: center; gap: 10px;
    font-family: "Montserrat", Arial, sans-serif;
    font-weight: 800;
    font-size: 24px;
    color: var(--navy);
  }
  .front-brand .brand-dot { background: var(--navy); width: 16px; height: 16px; }
  .front-rule {
    position: absolute;
    top: 118px; right: 36px;
    width: 300px; height: 1px; background: var(--rule);
  }
  .service-area {
    position: absolute;
    top: 140px; right: 36px;
    text-align: right;
    font-size: 13px;
    line-height: 1.35;
    color: var(--ink);
  }
  .person {
    position: absolute;
    left: 40px; top: 178px;
  }
  .person-name {
    font-family: "Montserrat", Arial, sans-serif;
    font-weight: 800;
    font-size: 19px;
    color: var(--navy);
    line-height: 1.1;
  }
  .person-title { font-size: 13px; color: var(--red); }
  .person-rule { width: 250px; height: 1px; background: var(--rule); margin: 6px 0 8px; }
  .contact-list { list-style: none; font-size: 12.5px; color: var(--ink); line-height: 1.55; }
  .contact-list li { display: flex; align-items: center; gap: 8px; }
  .contact-list svg { width: 12px; height: 12px; flex: none; fill: var(--navy-deep); }
  .band-navy {
    position: absolute; left: 0; bottom: 0;
    width: 76%; height: 20px; background: var(--navy);
  }
  .band-red {
    position: absolute; right: 0; bottom: 0;
    width: 23%; height: 20px; background: var(--red);
  }
</style>
</head>
<body>

  <section class="card card-back" aria-label="Back of card">
    <div class="back-brand"><span class="brand-dot"></span>Harborline Energy</div>
    <p class="tagline">Harborline Energy, Powering America's Oil &amp; Gas fields.</p>
    <p class="back-copy">Frac fueling is what we do. We understand how important diesel fuel is to your operation, which is why our main service line is Frac fueling. We assure our supply and stand by our service</p>
  </section>

  <section class="card card-front" aria-label="Front of card">
    <div class="front-brand"><span class="brand-dot"></span>Harborline Energy</div>
    <div class="front-rule"></div>
    <p class="service-area">Servicing the Powder River<br>DJ basin &amp; Bakken formations</p>

    <div class="person">
      <p class="person-name">Dale Menschow</p>
      <p class="person-title">Owner/CEO</p>
      <div class="person-rule"></div>
      <ul class="contact-list">
        <li><svg viewBox="0 0 12 12"><path d="M3 0h6a1 1 0 0 1 1 1v10a1 1 0 0 1-1 1H3a1 1 0 0 1-1-1V1a1 1 0 0 1 1-1zm0 1.5v8h6v-8zM6 10.2a.6.6 0 1 0 0 1.2.6.6 0 0 0 0-1.2z"/></svg>555.318.4076</li>
        <li><svg viewBox="0 0 12 12"><path d="M0 2h12v8H0zm1 1v.4l5 3.3 5-3.3V3zm0 1.6V9h10V4.6L6 7.9z"/></svg>Dmenschow@harborlineenergy.example</li>
        <li><svg viewBox="0 0 12 12"><path d="M6 0a6 6 0 1 1 0 12A6 6 0 0 1 6 0zm0 1.2a4.8 4.8 0 0 0-1 9.5V8.5L3.5 7V5l2-1 1 1H8l.5-2-1-1.6A4.8 4.8 0 0 0 6 1.2z"/></svg>www.Harborlineenergy.example</li>
      </ul>
    </div>

    <div class="band-navy"></div>
    <div class="band-red"></div>
  </section>

</body>
</html>
```